VMR business card

Need a business card for a company that provides instructional design and elearning development services. The website is here: http://vantmoro.studio/

I'm attaching a current logo, as well as the old business card design. While I like to keep it clean, the old design is too simplistic for my liking. The only idea I want to reuse from the old design is placing industry jargon on the back of the card, just need a better way to present it. But if you have other ideas for the back--feel free to experiment.

Please use the colors complementary to the color we have on the website. Thank you!

```html
<!DOCTYPE html>
<html lang="en">
<head>
<meta charset="utf-8">
<title>VMR business card</title>
<link rel="stylesheet" href="https://fonts.googleapis.com/css2?family=Source+Sans+3:wght@400;600;700&display=swap">
<style>
  :root {
    --teal: #16b3ae;
    --teal-deep: #0fa19d;
    --sand: #d8c98c;
    --gold: #d6c57d;
    --ink: #2e3a3a;
    --white: #ffffff;
    --stage: #e6e7e7;
  }
  * { box-sizing: border-box; margin: 0; padding: 0; }
  html, body {
    width: 1200px; height: 716px; overflow: hidden;
    background: var(--stage);
    font-family: "Source Sans 3", "Myriad Pro", sans-serif;
  }
  .card {
    position: absolute;
    width: 500px; height: 300px;
    border-radius: 3px;
    box-shadow: 0 6px 18px rgba(0,0,0,.18);
    overflow: hidden;
  }

  /* Back of card: services */
  .card-back {
    left: 70px; top: 130px;
    background: linear-gradient(200deg, var(--teal) 0%, #6fc2b0 50%, var(--sand) 100%);
    color: var(--white);
  }
  .world-map {
    position: absolute; left: 60px; top: 60px; width: 380px; height: 200px;
    background: radial-gradient(ellipse at center, rgba(255,255,255,.18), rgba(255,255,255,0) 70%);
  }
  .brand-mark {
    position: absolute; left: 0; right: 0; top: 52px;
    display: flex; justify-content: center; align-items: center; gap: 10px;
    font-weight: 700; font-size: 34px; letter-spacing: 2px;
  }
  .brand-mark .dot { width: 14px; height: 14px; background: var(--white); }
  .services {
    position: absolute; left: 0; right: 0; top: 118px;
    display: flex; flex-direction: column; align-items: center; gap: 5px;
  }
  .service-tag {
    background: var(--teal-deep);
    padding: 1px 8px;
    font-size: 15px; line-height: 19px;
    border-radius: 2px;
  }
  .back-url {
    position: absolute; left: 0; right: 0; top: 232px;
    text-align: center; font-size: 14px;
  }

  /* Front of card: contact */
  .card-front {
    left: 630px; top: 260px;
    background: var(--white);
  }
  .contact-panel {
    position: absolute; left: 0; top: 0; width: 240px; height: 100%;
    background: var(--teal);
    color: var(--white);
  }
  .divider { position: absolute; left: 240px; top: 0; }
  .person { position: absolute; right: 14px; top: 28px; text-align: right; }
  .person-name {
    color: var(--gold); font-weight: 700; font-size: 16px; letter-spacing: .5px;
  }
  .person-role { color: var(--ink); font-size: 13px; }
  .contacts {
    position: absolute; right: 14px; bottom: 40px;
    list-style: none; font-size: 13px; line-height: 20px; text-align: right;
  }
  .contacts li { display: flex; justify-content: flex-end; align-items: center; gap: 6px; }
  .contacts svg { width: 13px; height: 13px; }
  .front-brand {
    position: absolute; left: 290px; top: 84px;
    display: flex; align-items: center; gap: 10px;
    color: var(--teal); font-weight: 700; font-size: 40px; letter-spacing: 2px;
  }
  .front-brand .dot { width: 14px; height: 14px; background: var(--teal); }
  .faint-block {
    position: absolute; left: 330px; top: 170px; width: 190px; height: 150px;
    background: rgba(22,179,174,.08);
  }
</style>
</head>
<body>

<section class="card card-back" aria-label="Card back">
  <div class="world-map" role="img" aria-label="Dotted world map background"></div>
  <div class="brand-mark"><span class="dot"></span>VMR</div>
  <div class="services">
    <span class="service-tag">Instructional Design</span>
    <span class="service-tag">Elearning Development | Mobile Learning</span>
    <span class="service-tag">Insructor-LED Training</span>
  </div>
  <p class="back-url">www.vantmoro.studio</p>
</section>

<section class="card card-front" aria-label="Card front">
  <div class="contact-panel">
    <div class="person">
      <p class="person-name">MARCUS FELDHAVEN</p>
      <p class="person-role">managing director</p>
    </div>
    <ul class="contacts">
      <li>555-014-2783
        <svg viewBox="0 0 16 16"><circle cx="8" cy="8" r="8" fill="#d6c57d"/><path d="M5 4h2l1 2-1 1c.5 1 1 1.5 2 2l1-1 2 1v2c-4 0-7-3-7-7z" fill="#fff"/></svg></li>
      <li>mfeldhaven@vantmoro.studio
        <svg viewBox="0 0 16 16"><circle cx="8" cy="8" r="8" fill="#d6c57d"/><rect x="4" y="5" width="8" height="6" fill="#fff"/><path d="M4 5l4 3 4-3" stroke="#d6c57d" fill="none"/></svg></li>
      <li>www.vantmoro.studio
        <svg viewBox="0 0 16 16"><circle cx="8" cy="8" r="8" fill="#d6c57d"/><circle cx="8" cy="8" r="4.5" fill="none" stroke="#fff"/><path d="M3.5 8h9M8 3.5v9" stroke="#fff"/></svg></li>
    </ul>
  </div>
  <svg class="divider" width="16" height="300" viewBox="0 0 16 300">
    <path d="M0 0h7v38l7 8-7 8v246H0z" fill="#d6c57d"/>
  </svg>
  <div class="faint-block"></div>
  <div class="front-brand"><span class="dot"></span>VMR</div>
</section>

</body>
</html>
```